SEO AND WEB DESIGN COMPANY BUSINESS CARD DESIGN

I need an eye catching , simple business card design that will match my logo . I need 2 versions of it ( white background and black background) - SOME PEOPLE DID NOT GET IT AND SENDING US FRONT WHITE BACK WHITE VERSIONS WHICH IS NOT CORRECT.

ONE VERSION SHOULD BE BACK AND FRONT ALL BLACK , SECOND VERSION SHOULD BE BACK AND FRONT ALL WHITE

logo psd files are attached for both versions. The business card is going to have : First Name- Last name - position - phone numbers

```html
<!DOCTYPE html>
<html lang="en">
<head>
<meta charset="utf-8">
<title>Northlane Digital – Business Card</title>
<link href="https://fonts.googleapis.com/css2?family=Roboto:wght@400;500&family=Roboto+Condensed:wght@400&display=swap" rel="stylesheet">
<style>
  :root {
    --backdrop: #dcdcdc;
    --paper: #ffffff;
    --ink: #111111;
    --ink-soft: #555555;
    --accent: #3d9bf5;
    --night: #000000;
    --divider: #b8b8b8;
  }
  * { box-sizing: border-box; margin: 0; padding: 0; }
  html, body { width: 1200px; height: 1200px; overflow: hidden; }
  body {
    background: var(--backdrop);
    font-family: "Roboto", Arial, sans-serif;
    position: relative;
  }
  .card {
    position: absolute;
    left: 262px;
    width: 686px;
    height: 392px;
    overflow: hidden;
  }
  .card--front { top: 165px; background: var(--paper); }
  .card--back { top: 653px; background: var(--night); }

  .brand-name {
    position: absolute;
    font-family: "Roboto Condensed", Arial, sans-serif;
    font-weight: 400;
    white-space: nowrap;
    line-height: 1;
  }
  .card--front .brand-name {
    left: 34px;
    top: 180px;
    width: 286px;
    text-align: center;
    font-size: 30px;
    letter-spacing: 0.5px;
    color: var(--ink);
  }
  .card--back .brand-name {
    left: 0;
    right: 0;
    top: 160px;
    text-align: center;
    font-size: 40px;
    letter-spacing: 1px;
    color: var(--accent);
  }

  .divider {
    position: absolute;
    left: 342px;
    top: 79px;
    width: 1px;
    height: 240px;
    background: var(--divider);
  }

  .contact { position: absolute; left: 368px; top: 94px; }
  .contact__name { font-size: 26px; font-weight: 500; color: var(--accent); line-height: 1.15; }
  .contact__role { font-size: 17px; font-weight: 500; color: var(--ink); line-height: 1.2; }
  .contact__address { margin-top: 13px; font-size: 16px; color: var(--ink-soft); line-height: 21px; }
  .contact__lines { list-style: none; margin-top: 10px; }
  .contact__lines li {
    display: flex; align-items: center; gap: 11px;
    font-size: 16px; color: var(--ink-soft); line-height: 21.5px;
  }
  .contact__lines li.email { font-family: "Roboto Condensed", Arial, sans-serif; }
  .contact__lines svg { width: 16px; height: 16px; flex: none; fill: var(--accent); }

  .footer-band { position: absolute; left: 0; bottom: 0; width: 686px; height: 40px; }
  .footer-band__url {
    position: absolute; left: 23px; bottom: 6px;
    font-family: "Roboto Condensed", Arial, sans-serif;
    font-size: 16px; color: var(--paper);
  }

  .back-url {
    position: absolute; left: 0; right: 0; top: 338px;
    text-align: center; font-size: 18px; letter-spacing: 8px; color: var(--paper);
  }
</style>
</head>
<body>

<section class="card card--front" aria-label="Business card front">
  <div class="brand-name">NORTHLANE DIGITAL</div>
  <div class="divider"></div>

  <div class="contact">
    <h1 class="contact__name">Daniel Harper</h1>
    <p class="contact__role">President</p>
    <p class="contact__address">412 Willow Crest Road<br>Fairbanks, Alaska 99701</p>
    <ul class="contact__lines">
      <li><svg viewBox="0 0 16 16"><path d="M3.5 1.5l2.5 0 1 3.5-1.7 1.2c.8 1.8 2.2 3.2 4 4l1.2-1.7 3.5 1v2.5c0 .8-.7 1.5-1.5 1.5C7 13.5 2 8.5 2 3c0-.8.7-1.5 1.5-1.5z"/></svg>555-214-7730</li>
      <li><svg viewBox="0 0 16 16"><path d="M4.5 0h7a1.5 1.5 0 011.5 1.5v13a1.5 1.5 0 01-1.5 1.5h-7A1.5 1.5 0 013 14.5v-13A1.5 1.5 0 014.5 0zM5 2v10.5h6V2z"/></svg>555-318-6604</li>
      <li><svg viewBox="0 0 16 16"><path d="M4 1h6l2 2v3H4zM1 7h14v6H1zm3 4v4h8v-4z"/></svg>555-427-9152</li>
      <li class="email"><svg viewBox="0 0 16 16"><path d="M1 3h14v10H1zm1.5 1.5v.3L8 8.5l5.5-3.7v-.3zm0 2v5h11v-5L8 10.2z"/></svg>info@northlanedigital.com</li>
    </ul>
  </div>

  <svg class="footer-band" viewBox="0 0 686 40" aria-hidden="true">
    <polygon points="0,11 280,11 300,29 686,29 686,40 0,40" fill="var(--accent)"/>
    <line x1="296" y1="22" x2="664" y2="22" stroke="var(--ink)" stroke-width="3"/>
    <polygon points="662,14 677,22 662,30" fill="var(--ink)"/>
  </svg>
  <div class="footer-band__url">www.northlanedigital.com</div>
</section>

<section class="card card--back" aria-label="Business card back">
  <div class="brand-name">NORTHLANE DIGITAL</div>
  <p class="back-url">www.northlanedigital.com</p>
</section>

</body>
</html>
```